Business Card Design Project

Hello,

We have just created our new COMPANY LOGO via Pixel Harbor and would not like to turn our attention to new Business Cards.

We are a printing company based in Singapore & Las Vegas. We specialize in blue-print printing for the Architectural, Engineering and Construction industries

The design should be simple, professional, clean and organized.

The Business Cards should "pop" when seen and will hopefully be something that makes you look twice.

We have two different Pan-tones that we use for our company, feel free to use them if you think they will work for your design?

Orange: PMS 021
Gray: PMS 431

I have attached our current logo for your use and reference which should obvious be on our business cards.

Considering we have two locations on different continents, we need business cards templates where the address details need to be interchangeable for each different location (total 2)

First one:
38 Merrow Lane #03-11 to #03-15
Singapore 528473
Tel : +65 6847-3920
Fax : +65 6843-7702

Second one:
2381 W. Tanfield Rd, Suite 204
Las Vegas, Nevada 89152
Tel : (702) 555-4137
Fax : (702) 555-4189

We would also like to list a few of our key services on the card. Here are a few examples to get you going.

Plan Printing & Plotting
Digital Colour Printing
Cadline Printing
Specialty Book Making
Scanning & Archiving
Collection & Delivey

This is the first time i have requested for business cards to be created so please let me know if you require any additional information.
Many Thanks,
Tobin
Updates

Project Deadline Extended
Reason: It took us longer than expected to finalize our Company Logo We look forward to receiving your designs.

Target Market(s)

Our Target Market is construction related people.
Construction
Architecture
Engineering

Industry/Entity Type

Printing

Font styles to use
Other font styles liked:
• Times New Roman

Colors
faa54b
ffffff

Requirements
Must have
• The business card must have our Company Logo (attached)
The font used must be Times New Roman
Should not have
• Playful images of print designs and/or logos

```html
<!DOCTYPE html>
<html lang="en">
<head>
<meta charset="utf-8">
<title>Kestrel Print Works — Business Card</title>
<link rel="stylesheet" href="https://fonts.googleapis.com/css2?family=Roboto+Condensed:wght@400;700&family=Tinos:wght@400&display=swap">
<style>
  :root {
    --stage: #2b2b2d;
    --card: #3a3a3c;
    --orange: #f0973a;
    --white: #ffffff;
    --muted: #d6d6d6;
    --rule: #8a8a8c;
    --gear-light: #6b6b68;
    --gear-dark: #555553;
  }
  * { box-sizing: border-box; margin: 0; padding: 0; }
  html, body { width: 1200px; height: 800px; overflow: hidden; }
  body {
    background: var(--stage);
    display: flex;
    align-items: center;
    justify-content: center;
  }
  .business-card {
    position: relative;
    width: 1050px;
    height: 600px;
    background: var(--card);
    overflow: hidden;
    font-family: "Roboto Condensed", Arial, sans-serif;
    color: var(--white);
  }
  .tool-illustration {
    position: absolute;
    left: 0;
    top: 40px;
    width: 330px;
    height: 230px;
    background: linear-gradient(160deg, #f4a24a, #e68a2e);
    border-radius: 0 115px 115px 0;
  }
  .company-block {
    position: absolute;
    left: 370px;
    top: 70px;
    width: 420px;
  }
  .company-name {
    font-weight: 700;
    font-size: 50px;
    line-height: 1.02;
    letter-spacing: 0.5px;
  }
  .company-tagline {
    margin-top: 10px;
    font-size: 17px;
    color: var(--muted);
    padding-bottom: 10px;
    border-bottom: 1.5px solid var(--rule);
  }
  .contact-list {
    position: absolute;
    left: 370px;
    top: 300px;
    width: 320px;
    list-style: none;
    font-size: 22px;
    color: var(--muted);
  }
  .contact-item {
    display: flex;
    align-items: flex-start;
    gap: 14px;
    padding: 8px 0;
    border-bottom: 1.5px solid var(--rule);
  }
  .contact-item:last-child { border-bottom: none; }
  .contact-icon { width: 20px; height: 22px; flex: none; margin-top: 2px; }
  .address-lines { line-height: 1.25; }
  .brand-mark {
    position: absolute;
    right: 70px;
    top: 90px;
    display: flex;
    align-items: center;
    gap: 10px;
  }
  .brand-square { width: 14px; height: 14px; background: var(--white); }
  .brand-name {
    font-family: "Tinos", "Times New Roman", serif;
    font-size: 24px;
    color: var(--white);
  }
  .gear-decoration {
    position: absolute;
    right: 0;
    bottom: 0;
    width: 340px;
    height: 220px;
    background: radial-gradient(circle at 70% 60%, var(--gear-light), var(--gear-dark) 60%, var(--card) 90%);
    border-top-left-radius: 160px;
    opacity: 0.8;
  }
</style>
</head>
<body>
  <article class="business-card">
    <div class="tool-illustration" role="img" aria-label="Orange adjustable wrench gripping a gear"></div>

    <header class="company-block">
      <h1 class="company-name">Kestrel Print<br>Works</h1>
      <p class="company-tagline">A member of the KPW Group of Companies</p>
    </header>

    <ul class="contact-list">
      <li class="contact-item">
        <svg class="contact-icon" viewBox="0 0 20 22" aria-hidden="true">
          <path d="M5 2 L8 2 L9 7 L7 8.5 C8 11.5 10 13.5 13 14.5 L14.5 12.5 L19 13.5 L19 17 C19 18.5 17.5 19.5 16 19.5 C9 19 3 13 2.5 6 C2.5 4 3.5 2 5 2 Z" fill="var(--orange)"/>
        </svg>
        <span>(702) 555-4137</span>
      </li>
      <li class="contact-item">
        <svg class="contact-icon" viewBox="0 0 20 22" aria-hidden="true">
          <rect x="2" y="8" width="16" height="11" rx="2" fill="var(--orange)"/>
          <rect x="5" y="2" width="10" height="8" fill="var(--orange)"/>
          <rect x="6" y="3.5" width="8" height="1.2" fill="var(--card)"/>
          <rect x="6" y="6" width="8" height="1.2" fill="var(--card)"/>
        </svg>
        <span>(702) 555-4189</span>
      </li>
      <li class="contact-item">
        <svg class="contact-icon" viewBox="0 0 20 22" aria-hidden="true">
          <path d="M10 1 C5.5 1 3 4.3 3 7.8 C3 12.5 10 21 10 21 C10 21 17 12.5 17 7.8 C17 4.3 14.5 1 10 1 Z" fill="var(--orange)"/>
          <circle cx="10" cy="8" r="2.8" fill="var(--card)"/>
        </svg>
        <span class="address-lines">2381 W. Tanfield Rd, Suite 204<br>Las Vegas, Nevada 89152</span>
      </li>
    </ul>

    <div class="brand-mark">
      <span class="brand-square"></span>
      <span class="brand-name">Kestrel Print Works</span>
    </div>

    <div class="gear-decoration" role="img" aria-label="Cluster of grey interlocking gears"></div>
  </article>
</body>
</html>
```